VELMORA perfume bottle needs a label design

We are a fragrance company called VELMORA. We have 16 perfumes in four collections: Oud, Sweet, France, and Oriental collections. Each collection has four perfumes. The bottles are standard for all 16 perfumes with the same cap. It's a 50 ml glass bottle with a BLACK cap, (not as mentioned in the pics). I will attach the bottle pictures, as well as the perfume boxes so you can see the colours. I will attach our logo as well to go on the front side of the bottle.
Please note that the sides of the bottle are straight, but the front and back are curved. Please also note that the pics that have the boxes are old and we have changed the names of the perfumes. First, they no longer say "collection" on the bottle. Second, each collection has four perfumes numbered from 1 to 4, instead of 1 to 16 for all perfumes, for example: Oud 1, France 1, Sweet 4 and so on, but with Romanian numbers.
We are going to colour and print on these bottles, so we are looking for one design for all collections but each collection will have its colour.
Other info you might use:
bottles are 50 ml, made in France, EDP or Eau De Parfum
IN THE ATTACHMENTS
Please refer to File 1 to 6 for the images of our perfume bottle containers.
File 8 is where you can find our logo for VELMORA
Updates
Industry/Entity Type
It Company
Look and feel

```html
<!DOCTYPE html>
<html lang="en">
<head>
<meta charset="utf-8">
<title>VELMORA — Label Collection</title>
<link rel="stylesheet" href="https://fonts.googleapis.com/css2?family=Tinos:ital,wght@0,400;0,700;1,400;1,700&family=Montserrat:wght@300&display=swap">
<style>
  :root {
    --paper: #ffffff;
    --ink: #000000;
    --numeral: #8f8f8f;
    --gold: #c39a2c;
    --gold-light: #d9b24a;
    --glass: #e3ebe4;
    --glass-deep: #b9c8bd;
    --cap: #2a211c;
  }
  * { margin: 0; padding: 0; box-sizing: border-box; }
  html, body { width: 1200px; height: 869px; overflow: hidden; background: var(--paper); }
  .canvas { position: relative; width: 1200px; height: 869px; background: var(--paper); }

  .label-grid {
    position: absolute; left: 3px; top: 3px;
    display: grid;
    grid-template-columns: repeat(5, 195px);
    grid-template-rows: repeat(3, 284px);
    column-gap: 4px; row-gap: 5px;
  }
  .label {
    position: relative;
    border: 2px solid var(--ink);
    outline: 1px solid var(--ink);
    outline-offset: 1px;
    background: var(--paper);
    font-family: "Tinos", "Times New Roman", serif;
    color: var(--ink);
  }
  .label__brand {
    position: absolute; left: 8px; top: 10px;
    display: flex; flex-direction: column; align-items: center; gap: 4px;
  }
  .label__brand-mark {
    width: 26px; height: 26px; border-radius: 50%; background: var(--ink);
  }
  .label__brand-name {
    font-family: "Tinos", "Times New Roman", serif;
    font-size: 10px; letter-spacing: 0.5px; color: var(--gold);
  }
  .label__specs {
    position: absolute; right: 6px; top: 4px;
    text-align: right; line-height: 12px;
  }
  .label__specs .type { font-size: 10.5px; }
  .label__specs .origin { font-size: 6px; }
  .label__specs .origin b { font-size: 10.5px; font-weight: 400; }
  .label__specs .volume { font-size: 9px; }
  .label__numeral {
    position: absolute; left: 0; right: 0; top: 86px;
    text-align: center;
    font-style: italic; font-weight: 700;
    font-size: 88px; line-height: 1;
    color: var(--numeral);
  }
  .label__collection {
    position: absolute; left: 0; right: 0; bottom: 4px;
    text-align: center;
    font-size: 42px; line-height: 1;
    white-space: nowrap;
  }
  .label__collection--oud { font-size: 54px; bottom: 0; }
  .label__collection--oriental { font-size: 31px; bottom: 8px; }

  .brand-vertical {
    position: absolute; left: 1040px; top: 12px;
    width: 80px; height: 390px;
    display: flex; align-items: center; justify-content: center;
  }
  .brand-vertical span {
    display: block;
    transform: rotate(90deg);
    white-space: nowrap;
    font-family: "Montserrat", "Helvetica Neue", sans-serif;
    font-weight: 300;
    font-size: 62px; letter-spacing: 8px;
    color: var(--gold);
  }

  .bottle-visual {
    position: absolute; left: 1012px; top: 410px;
    width: 180px; height: 455px;
    border-radius: 14px;
    background: linear-gradient(180deg, var(--cap) 0%, var(--cap) 26%, var(--gold-light) 27%, var(--gold) 29%, var(--glass) 30%, var(--glass-deep) 100%);
  }
</style>
</head>
<body>
<main class="canvas">
  <section class="label-grid">
    <!-- Row 1 -->
    <article class="label">
      <div class="label__brand"><span class="label__brand-mark"></span><span class="label__brand-name">VELMORA</span></div>
      <div class="label__specs"><div class="type">Eua De Parfum</div><div class="origin">Made in: <b>France</b></div><div class="volume">50ml</div></div>
      <div class="label__numeral">-I-</div>
      <div class="label__collection">FRANCE</div>
    </article>
    <article class="label">
      <div class="label__brand"><span class="label__brand-mark"></span><span class="label__brand-name">VELMORA</span></div>
      <div class="label__specs"><div class="type">Eua De Parfum</div><div class="origin">Made in: <b>France</b></div><div class="volume">50ml</div></div>
      <div class="label__numeral">-II-</div>
      <div class="label__collection">FRANCE</div>
    </article>
    <article class="label">
      <div class="label__brand"><span class="label__brand-mark"></span><span class="label__brand-name">VELMORA</span></div>
      <div class="label__specs"><div class="type">Eua De Parfum</div><div class="origin">Made in: <b>France</b></div><div class="volume">50ml</div></div>
      <div class="label__numeral">-III-</div>
      <div class="label__collection">FRANCE</div>
    </article>
    <article class="label">
      <div class="label__brand"><span class="label__brand-mark"></span><span class="label__brand-name">VELMORA</span></div>
      <div class="label__specs"><div class="type">Eua De Parfum</div><div class="origin">Made in: <b>France</b></div><div class="volume">50ml</div></div>
      <div class="label__numeral">-IV-</div>
      <div class="label__collection">FRANCE</div>
    </article>
    <article class="label">
      <div class="label__brand"><span class="label__brand-mark"></span><span class="label__brand-name">VELMORA</span></div>
      <div class="label__specs"><div class="type">Eua De Parfum</div><div class="origin">Made in: <b>France</b></div><div class="volume">50ml</div></div>
      <div class="label__numeral">-I-</div>
      <div class="label__collection label__collection--oriental">ORIENTAL</div>
    </article>

    <!-- Row 2 -->
    <article class="label">
      <div class="label__brand"><span class="label__brand-mark"></span><span class="label__brand-name">VELMORA</span></div>
      <div class="label__specs"><div class="type">Eua De Parfum</div><div class="origin">Made in: <b>France</b></div><div class="volume">50ml</div></div>
      <div class="label__numeral">-I-</div>
      <div class="label__collection">SWEET</div>
    </article>
    <article class="label">
      <div class="label__brand"><span class="label__brand-mark"></span><span class="label__brand-name">VELMORA</span></div>
      <div class="label__specs"><div class="type">Eua De Parfum</div><div class="origin">Made in: <b>France</b></div><div class="volume">50ml</div></div>
      <div class="label__numeral">-II-</div>
      <div class="label__collection">SWEET</div>
    </article>
    <article class="label">
      <div class="label__brand"><span class="label__brand-mark"></span><span class="label__brand-name">VELMORA</span></div>
      <div class="label__specs"><div class="type">Eua De Parfum</div><div class="origin">Made in: <b>France</b></div><div class="volume">50ml</div></div>
      <div class="label__numeral">-III-</div>
      <div class="label__collection">SWEET</div>
    </article>
    <article class="label">
      <div class="label__brand"><span class="label__brand-mark"></span><span class="label__brand-name">VELMORA</span></div>
      <div class="label__specs"><div class="type">Eua De Parfum</div><div class="origin">Made in: <b>France</b></div><div class="volume">50ml</div></div>
      <div class="label__numeral">-IV-</div>
      <div class="label__collection">SWEET</div>
    </article>
    <article class="label">
      <div class="label__brand"><span class="label__brand-mark"></span><span class="label__brand-name">VELMORA</span></div>
      <div class="label__specs"><div class="type">Eua De Parfum</div><div class="origin">Made in: <b>France</b></div><div class="volume">50ml</div></div>
      <div class="label__numeral">-II-</div>
      <div class="label__collection label__collection--oriental">ORIENTAL</div>
    </article>

    <!-- Row 3 -->
    <article class="label">
      <div class="label__brand"><span class="label__brand-mark"></span><span class="label__brand-name">VELMORA</span></div>
      <div class="label__specs"><div class="type">Eua De Parfum</div><div class="origin">Made in: <b>France</b></div><div class="volume">50ml</div></div>
      <div class="label__numeral">-I-</div>
      <div class="label__collection label__collection--oud">OUD</div>
    </article>
    <article class="label">
      <div class="label__brand"><span class="label__brand-mark"></span><span class="label__brand-name">VELMORA</span></div>
      <div class="label__specs"><div class="type">Eua De Parfum</div><div class="origin">Made in: <b>France</b></div><div class="volume">50ml</div></div>
      <div class="label__numeral">-II-</div>
      <div class="label__collection label__collection--oud">OUD</div>
    </article>
    <article class="label">
      <div class="label__brand"><span class="label__brand-mark"></span><span class="label__brand-name">VELMORA</span></div>
      <div class="label__specs"><div class="type">Eua De Parfum</div><div class="origin">Made in: <b>France</b></div><div class="volume">50ml</div></div>
      <div class="label__numeral">-III-</div>
      <div class="label__collection label__collection--oud">OUD</div>
    </article>
    <article class="label">
      <div class="label__brand"><span class="label__brand-mark"></span><span class="label__brand-name">VELMORA</span></div>
      <div class="label__specs"><div class="type">Eua De Parfum</div><div class="origin">Made in: <b>France</b></div><div class="volume">50ml</div></div>
      <div class="label__numeral">-IV-</div>
      <div class="label__collection label__collection--oud">OUD</div>
    </article>
    <article class="label">
      <div class="label__brand"><span class="label__brand-mark"></span><span class="label__brand-name">VELMORA</span></div>
      <div class="label__specs"><div class="type">Eua De Parfum</div><div class="origin">Made in: <b>France</b></div><div class="volume">50ml</div></div>
      <div class="label__numeral">-III-</div>
      <div class="label__collection label__collection--oriental">ORIENTAL</div>
    </article>
  </section>

  <div class="brand-vertical"><span>VELMORA</span></div>

  <div class="bottle-visual" role="img" aria-label="Product photo of the 50 ml glass perfume bottle with dark wooden cap and gold collar, wearing the Oriental IV label"></div>
</main>
</body>
</html>
```